Velnor Group: Business Card for a high end technology company

We need a cool new design for our business cards using our cloud logo. We are a technology consulting business. We pride ourselves on be the best of the best. We mainly focus on cloud solutions and managed services. We need a business card that sets us apart from the other technology companies in the area and allows us to stand out.

Target Market(s)

Technology departments, CIO, CEOs, and Information Technology Staff.

Industry/Entity Type

Information Technology

Contact Information for Business Card

Must have the logo and our name.
Must have employee name, email address, office phone, cell phone and website.
Need to have all info on one side a cool design on backside.

Font styles to use
Serif
Sans Serif

Requirements
Must have
• Must have the logo and our name.
• Must have employee name, email address, office phone, cell phone and website.
• Need to have all info on one side a cool design on back side.
• Must be a crisp clean design, not too busy or confusing.

```html
<!DOCTYPE html>
<html lang="en">
<head>
<meta charset="utf-8">
<title>Velnor Group – Business Card</title>
<link rel="stylesheet" href="https://fonts.googleapis.com/css2?family=Questrial&family=Open+Sans:wght@400;600&display=swap">
<style>
  :root {
    --backdrop: #e9ebee;
    --card: #ffffff;
    --ink: #3a3a3c;
    --ink-soft: #5c5c60;
    --accent: #3fa9e0;
    --accent-light: #8fd3f4;
    --accent-deep: #2b8fd0;
    --rule: #d8d8dc;
  }
  * { box-sizing: border-box; margin: 0; padding: 0; }
  html, body { width: 1200px; height: 900px; overflow: hidden; }
  body {
    background: var(--backdrop);
    font-family: "Open Sans", Arial, sans-serif;
    color: var(--ink);
    position: relative;
  }
  .card {
    position: absolute;
    left: 270px;
    width: 660px;
    height: 380px;
    background: var(--card);
    border-radius: 22px;
    overflow: hidden;
    box-shadow: 0 6px 18px rgba(0,0,0,0.12);
  }
  .card--front { top: 50px; }
  .card--back { top: 470px; }

  .brand {
    display: flex;
    align-items: center;
    gap: 14px;
    font-family: "Questrial", Arial, sans-serif;
    color: var(--ink);
  }
  .brand__dot {
    width: 30px; height: 30px;
    border-radius: 50%;
    background: var(--accent);
  }
  .brand__name { font-size: 52px; letter-spacing: 0.5px; }

  .card--front .brand-block {
    position: absolute;
    left: 0; right: 0; top: 140px;
    display: flex; flex-direction: column; align-items: center; gap: 10px;
  }
  .brand-block__web {
    font-family: "Open Sans", Arial, sans-serif;
    font-weight: 600;
    font-size: 15px;
    color: var(--ink);
    padding-left: 44px;
  }

  .swoosh { position: absolute; left: 0; top: 0; width: 660px; height: 380px; }

  .card--back .brand {
    position: absolute; left: 40px; top: 130px;
  }
  .card--back .brand__name { font-size: 40px; }
  .card--back .brand__dot { width: 24px; height: 24px; }

  .divider {
    position: absolute; left: 330px; top: 0;
    width: 1px; height: 280px;
    background: linear-gradient(to bottom, transparent, var(--rule) 25%, var(--rule) 80%, transparent);
  }

  .info { position: absolute; left: 360px; top: 36px; width: 280px; }
  .info__name {
    font-family: "Questrial", Arial, sans-serif;
    font-size: 22px; letter-spacing: 1px; color: var(--ink-soft);
  }
  .info__name span { color: var(--accent); }
  .info__title { font-size: 13px; color: var(--ink-soft); margin-top: 2px; }
  .info__address { margin-top: 52px; font-size: 13px; line-height: 1.45; color: var(--ink); }
  .contact { list-style: none; margin-top: 2px; font-size: 13px; line-height: 1.45; }
  .contact li { display: flex; align-items: center; gap: 8px; }
  .contact svg { width: 12px; height: 12px; fill: var(--ink); flex: none; }
</style>
</head>
<body>

<section class="card card--front" aria-label="Card front">
  <div class="brand-block">
    <div class="brand">
      <span class="brand__dot"></span>
      <span class="brand__name">Velnor Group</span>
    </div>
    <p class="brand-block__web">www.velnorgroup.com</p>
  </div>
</section>

<section class="card card--back" aria-label="Card back">
  <svg class="swoosh" viewBox="0 0 660 380" aria-hidden="true">
    <defs>
      <linearGradient id="swoosh-fill" x1="0" y1="0" x2="0" y2="1">
        <stop offset="0" stop-color="var(--accent)"/>
        <stop offset="1" stop-color="var(--accent-deep)"/>
      </linearGradient>
    </defs>
    <path d="M0 300 C 220 318, 480 300, 660 236 L660 380 L0 380 Z" fill="var(--accent-light)"/>
    <path d="M0 312 C 230 330, 480 312, 660 252 L660 380 L0 380 Z" fill="url(#swoosh-fill)"/>
  </svg>

  <div class="brand">
    <span class="brand__dot"></span>
    <span class="brand__name">Velnor Group</span>
  </div>

  <div class="divider"></div>

  <div class="info">
    <p class="info__name">YOUR<span>NAME</span></p>
    <p class="info__title">Title</p>
    <p class="info__address">1450 North Cedar Ridge Rd<br>Suite 210-318 Phoenix, AZ</p>
    <ul class="contact">
      <li><svg viewBox="0 0 24 24"><path d="M6.6 10.8a15 15 0 0 0 6.6 6.6l2.2-2.2c.3-.3.7-.4 1-.2 1.1.4 2.3.6 3.6.6.6 0 1 .4 1 1V20c0 .6-.4 1-1 1C10.6 21 3 13.4 3 4c0-.6.4-1 1-1h3.5c.6 0 1 .4 1 1 0 1.3.2 2.5.6 3.6.1.3 0 .7-.2 1z"/></svg>0412558071</li>
      <li><svg viewBox="0 0 24 24"><path d="M7 1h10a2 2 0 0 1 2 2v18a2 2 0 0 1-2 2H7a2 2 0 0 1-2-2V3a2 2 0 0 1 2-2zm0 3v14h10V4zm5 15.5a1.2 1.2 0 1 0 0 2.4 1.2 1.2 0 0 0 0-2.4z"/></svg>0412558071</li>
      <li><svg viewBox="0 0 24 24"><path d="M2 5h20v14H2zm2 2v.5l8 5 8-5V7zm0 2.8V17h16V9.8l-8 5z"/></svg>info@velnorgroup.com</li>
      <li><svg viewBox="0 0 24 24"><path d="M12 2a10 10 0 1 0 0 20 10 10 0 0 0 0-20zm6.9 9h-3a15 15 0 0 0-1.3-5.6A8 8 0 0 1 18.9 11zM12 4c.9 1.2 1.8 3.6 1.9 7h-3.8c.1-3.4 1-5.8 1.9-7zM9.4 5.4A15 15 0 0 0 8.1 11h-3a8 8 0 0 1 4.3-5.6zM5.1 13h3a15 15 0 0 0 1.3 5.6A8 8 0 0 1 5.1 13zM12 20c-.9-1.2-1.8-3.6-1.9-7h3.8c-.1 3.4-1 5.8-1.9 7zm2.6-1.4a15 15 0 0 0 1.3-5.6h3a8 8 0 0 1-4.3 5.6z"/></svg>www.velnorgroup.com</li>
    </ul>
  </div>
</section>

</body>
</html>
```